Spray Foam Company Business Card

We need a business card designed for our spray foam insulation and roof coatings business. We handle residential and commercial projects.
Construction
We would like it to say:
R & K Spray
with these bullet points
-foam insulation
-waterproofing roof system
-water proofing foundation systems
website is rksprayfoaminsulation.example (this was just purchased)
office phone : 630-482-9164
And 3 cards with names on them the names are :
Derek Halvorsen
Curtis Pennington
Rob Stallworth
maybe the bullet points can go on the back?
if you go this website it is another division of our company and you can see the font we use in the R & K. We do not want to use the same half circles that it has just the lettering
www.coatedrightforyears.example

```html
<!DOCTYPE html>
<html lang="en">
<head>
<meta charset="utf-8">
<title>R &amp; K Spray Business Card</title>
<link rel="stylesheet" href="https://fonts.googleapis.com/css2?family=Open+Sans:wght@400;700&family=Crimson+Text:ital,wght@1,600&display=swap">
<style>
  :root {
    --backdrop: #6b4226;
    --card: #ffffff;
    --ink-dark: #262626;
    --brand-green: #3daa3f;
    --text: #3a3a3a;
    --divider: #c8c8c8;
  }
  * { margin: 0; padding: 0; box-sizing: border-box; }
  html, body { width: 1200px; height: 406px; overflow: hidden; }
  body {
    background: var(--backdrop);
    position: relative;
    font-family: "Open Sans", Arial, sans-serif;
  }
  .card {
    position: absolute;
    top: 69px;
    width: 469px;
    height: 267px;
    background: var(--card);
    overflow: hidden;
    box-shadow: 0 2px 6px rgba(0,0,0,0.35);
  }
  .card--front { left: 122px; }
  .card--back { left: 609px; }
  .card__header { position: absolute; left: 0; top: 0; width: 469px; height: 100px; }
  .brand-name {
    position: absolute;
    top: 26px;
    font-family: "Open Sans", Arial, sans-serif;
    font-weight: 400;
    font-size: 32px;
    color: var(--brand-green);
    letter-spacing: 1px;
  }
  .card--front .brand-name { left: 42px; }
  .card--back .brand-name { left: 69px; }
  .person-name {
    position: absolute;
    left: 42px;
    top: 143px;
    font-family: "Crimson Text", Georgia, serif;
    font-style: italic;
    font-weight: 600;
    font-size: 22px;
    color: var(--text);
    white-space: nowrap;
  }
  .divider {
    position: absolute;
    left: 191px;
    top: 138px;
    width: 2px;
    height: 89px;
    background: var(--divider);
  }
  .contact {
    position: absolute;
    left: 205px;
    top: 146px;
    font-size: 12px;
    line-height: 16px;
    color: var(--text);
    white-space: nowrap;
  }
  .contact__group + .contact__group { margin-top: 8px; }
  .contact strong { font-weight: 700; }
  .services {
    position: absolute;
    left: 73px;
    top: 171px;
    list-style: none;
    font-weight: 700;
    font-size: 14.5px;
    line-height: 20px;
    color: var(--ink-dark);
  }
  .services li { position: relative; padding-left: 15px; }
  .services li::before {
    content: "";
    position: absolute;
    left: 1px;
    top: 8px;
    width: 5px;
    height: 5px;
    border-radius: 50%;
    background: var(--brand-green);
  }
</style>
</head>
<body>

<section class="card card--front">
  <svg class="card__header" viewBox="0 0 469 100" aria-hidden="true">
    <path fill="var(--ink-dark)" d="M0,0 H469 V22 C340,28 220,84 120,88 C80,90 40,84 0,74 Z"/>
    <path fill="var(--brand-green)" d="M188,87 C280,74 360,32 469,29 V38 C370,38 290,72 188,87 Z"/>
  </svg>
  <div class="brand-name">R &amp; K</div>
  <div class="person-name">Derek Halvorsen</div>
  <div class="divider"></div>
  <div class="contact">
    <div class="contact__group">
      <div>218 Maple Ridge Lane, Larkhaven, IL 60999</div>
      <div>Phone : 630-482-9164</div>
    </div>
    <div class="contact__group">
      <div><strong>Email :</strong> info@coatedrightforyears.example</div>
      <div><strong>Website :</strong> rksprayfoaminsulation.example</div>
    </div>
  </div>
</section>

<section class="card card--back">
  <svg class="card__header" viewBox="0 0 469 100" aria-hidden="true">
    <path fill="var(--ink-dark)" d="M0,0 H469 V22 C340,28 220,84 120,88 C80,90 40,84 0,74 Z"/>
    <path fill="var(--brand-green)" d="M188,87 C280,74 360,32 469,29 V38 C370,38 290,72 188,87 Z"/>
  </svg>
  <div class="brand-name">R &amp; K</div>
  <ul class="services">
    <li>foam insulation</li>
    <li>waterproofing roof system</li>
    <li>water proofing foundation systems</li>
  </ul>
</section>

</body>
</html>
```